Porch Light Podcast Cover Graphic

We need a graphic designed for a new podcast called "Porch Light." The graphic will be used on multiple podcasting platforms as the lead graphic advertising the podcast. The podcast consists of interviews of individuals sharing their life experiences including challenges, successes, lessons learned, and unexpected turns. The purpose of the podcast is to help listeners and participants learn from the life experiences of everyday neighbors. This podcast has a heavy Christian foundation on the parable of the good samaritan. We believe that through hearing the experiences of everyday neighbors, listeners can be strengthened, nourished, and aided to handle their own life challenges and trials. We would like the final design to be simple and reflective of the purpose and the parable of the good samaritan. The final design needs to have the title of the podcast, "Porch Light." We believe the best designs will limit the number of colors to less than 5 and will look good in a monochromatic version as well as a color version. We think the color white should be the main color. The graphic should be square in dimensions. We have considered having two hands grasping each other as if to lift the hand from below, but open to other creative simple takes to convey the lessons from the good samaritan.

```html
<!DOCTYPE html>
<html lang="en">
<head>
<meta charset="utf-8">
<title>Porch Light Podcast Cover</title>
<link rel="stylesheet" href="https://fonts.googleapis.com/css2?family=Marcellus&family=Montserrat:wght@300&display=swap">
<style>
  :root {
    --backdrop: #c4c4c4;
    --paper: #eeede4;
    --stripe: #ffffff;
    --band: #eb2d1d;
    --ink: #111111;
    --figure-tone: #3a3a3a;
    --ladder-tone: #b3231a;
  }
  * { margin: 0; padding: 0; box-sizing: border-box; }
  html, body {
    width: 714px;
    height: 1200px;
    overflow: hidden;
    background: var(--backdrop);
  }
  .cover {
    position: absolute;
    left: 37px;
    top: 280px;
    width: 640px;
    height: 640px;
    background: var(--paper);
    overflow: hidden;
  }
  .cover-art {
    position: absolute;
    inset: 0;
    width: 640px;
    height: 640px;
  }
  .title {
    position: absolute;
    left: 0;
    right: 0;
    top: 70px;
    text-align: center;
    font-family: "Marcellus", serif;
    color: var(--ink);
    font-weight: 400;
    line-height: 1;
  }
  .title-line {
    display: block;
    font-size: 92px;
    letter-spacing: 2px;
  }
  .title-line--second {
    margin-top: 2px;
  }
  .tagline {
    position: absolute;
    left: 0;
    right: 0;
    top: 592px;
    text-align: center;
    font-family: "Montserrat", sans-serif;
    font-weight: 300;
    font-size: 24px;
    letter-spacing: 16px;
    padding-left: 16px;
    color: var(--band);
    line-height: 1;
  }
</style>
</head>
<body>
  <main class="cover">
    <svg class="cover-art" viewBox="0 0 1278 1278" xmlns="http://www.w3.org/2000/svg">
      <polygon class="cover-stripe" points="0,717 1278,865 1278,901 0,738" fill="var(--stripe)"/>
      <polygon class="cover-band" points="0,738 1278,901 1278,1278 1245,1278 0,885" fill="var(--band)"/>
      <rect class="figure-area" x="570" y="700" width="40" height="100" fill="var(--figure-tone)"
            role="img" aria-label="Small silhouette of a man standing on the top edge of the red wall, casting a shadow"/>
      <rect class="ladder-area" x="482" y="835" width="225" height="275" fill="var(--ladder-tone)" opacity="0.55"
            role="img" aria-label="Two red ladders leaning against the wall in an A shape, with their shadow on the ground"/>
    </svg>
    <h1 class="title">
      <span class="title-line">PORCH</span>
      <span class="title-line title-line--second">LIGHT</span>
    </h1>
    <p class="tagline">PODCAST</p>
  </main>
</body>
</html>
```